New Business Card Design Project

Hi! I would like for you to design a business card for our aesthetic injections business. We offer Velmo, filler, skin care. I would like it to be elegant, feminine, modern and sleek/clean. I like black/gold foil/ivory/parchment colors. It can be either one or two sided. I would like matte black with gold foil logo on one side and ivory with gold foil information on the other side

Target Market(s)

target market is the discerning woman who wants to look her best

Industry/Entity Type

beauty

Contact Information for Business Card

logo, name, phone, email, website, instagram, facebook, location

Requirements
Must have
• logo and info
Nice to have
• the icons for cell, instagram, email, fb etc
Should not have
• images of people

```html
<!DOCTYPE html>
<html lang="en">
<head>
<meta charset="UTF-8">
<title>The Lumen Studio – Business Card</title>
<link href="https://fonts.googleapis.com/css2?family=Montserrat:wght@400;500;700&display=swap" rel="stylesheet">
<style>
  :root {
    --backdrop: #e9e4da;
    --matte-black: #0d0d0d;
    --ink: #111111;
    --ivory: #fbf1d1;
    --gold: #c9a24a;
    --gold-light: #e6cf86;
    --gold-deep: #a9822f;
  }
  * { box-sizing: border-box; margin: 0; padding: 0; }
  html, body {
    width: 1200px; height: 900px; overflow: hidden;
    background: var(--backdrop);
    font-family: "Montserrat", Arial, sans-serif;
  }
  .canvas {
    width: 1200px; height: 900px;
    display: flex; flex-direction: column; align-items: center; justify-content: center;
    gap: 24px;
  }
  .card {
    position: relative;
    width: 680px; height: 388px;
    overflow: hidden;
    box-shadow: 0 6px 18px rgba(0,0,0,0.18);
  }
  /* Front: matte black with gold mark */
  .card--front {
    background: var(--matte-black);
    display: flex; align-items: center; justify-content: center;
  }
  .brand-seal {
    width: 220px; height: 220px;
    border: 1.5px solid var(--gold);
    border-radius: 50%;
    display: flex; align-items: center; justify-content: center;
    text-align: center;
  }
  .brand-name {
    font-family: "Montserrat", Arial, sans-serif;
    font-weight: 500;
    color: var(--gold);
    letter-spacing: 0.18em;
    text-transform: uppercase;
    line-height: 1.5;
  }
  .card--front .brand-name { font-size: 19px; }

  /* Back: ivory with gold information */
  .card--back { background: var(--ivory); }
  .card-wave { position: absolute; inset: 0; width: 100%; height: 100%; }
  .contact {
    position: absolute; left: 54px; top: 70px;
    color: var(--ink);
  }
  .contact__name {
    font-size: 25px; font-weight: 700; letter-spacing: 0.02em;
    color: var(--gold); text-transform: uppercase;
  }
  .contact__role { font-size: 17px; font-weight: 500; margin-top: 2px; }
  .contact__lines { margin-top: 26px; list-style: none; }
  .contact__lines li {
    display: flex; align-items: center; gap: 10px;
    font-size: 17px; font-weight: 500; line-height: 1.55;
  }
  .contact__lines svg { width: 18px; height: 18px; flex: none; }
  .contact__address {
    margin-top: 34px; padding-left: 28px;
    font-size: 17px; font-weight: 500; line-height: 1.35;
  }
  .card--back .brand-seal {
    position: absolute; right: 52px; top: 34px;
    width: 168px; height: 168px;
  }
  .card--back .brand-name { font-size: 14px; }
  .website {
    position: absolute; right: 44px; bottom: 58px;
    font-size: 15px; font-weight: 500; color: var(--gold);
    letter-spacing: 0.02em;
  }
</style>
</head>
<body>
<main class="canvas">
  <section class="card card--front" aria-label="Card front">
    <div class="brand-seal">
      <span class="brand-name">The<br>Lumen<br>Studio</span>
    </div>
  </section>

  <section class="card card--back" aria-label="Card back">
    <svg class="card-wave" viewBox="0 0 680 388" preserveAspectRatio="none" aria-hidden="true">
      <defs>
        <linearGradient id="gold-foil" x1="0" y1="0" x2="1" y2="0">
          <stop offset="0" stop-color="#e6cf86"/>
          <stop offset="0.45" stop-color="#c9a24a"/>
          <stop offset="0.8" stop-color="#d9bb6a"/>
          <stop offset="1" stop-color="#a9822f"/>
        </linearGradient>
      </defs>
      <path d="M0,335 C170,330 330,292 430,228 C330,300 190,340 0,350 Z" fill="url(#gold-foil)"/>
      <path d="M0,388 L0,356 C210,352 380,305 500,232 C570,190 630,168 680,164 L680,388 Z" fill="#000"/>
    </svg>

    <div class="contact">
      <h1 class="contact__name">Adrian Vale</h1>
      <p class="contact__role">Managing Director</p>
      <ul class="contact__lines">
        <li>
          <svg viewBox="0 0 24 24" aria-hidden="true"><path fill="var(--gold)" d="M6.6 10.8a15.1 15.1 0 0 0 6.6 6.6l2.2-2.2a1 1 0 0 1 1-.25 11.4 11.4 0 0 0 3.6.57 1 1 0 0 1 1 1V20a1 1 0 0 1-1 1A17 17 0 0 1 3 4a1 1 0 0 1 1-1h3.5a1 1 0 0 1 1 1c0 1.25.2 2.45.57 3.57a1 1 0 0 1-.25 1z"/></svg>
          044-555 210 384
        </li>
        <li>
          <svg viewBox="0 0 24 24" aria-hidden="true"><path fill="var(--gold)" d="M2 5h20v14H2z"/><path fill="none" stroke="var(--ivory)" stroke-width="1.6" d="M2.5 5.5l9.5 7.5 9.5-7.5"/></svg>
          info@lumenstudio.com
        </li>
      </ul>
      <p class="contact__address">17 Ivory Lane, Suite 4<br>45210, Northvale</p>
    </div>

    <div class="brand-seal">
      <span class="brand-name">The<br>Lumen<br>Studio</span>
    </div>

    <p class="website">www.lumenstudio.com</p>
  </section>
</main>
</body>
</html>
```